Electrician Company Website Design

I am looking to get a website designed only. I do not need it converted ot html. I simply need the design in a psd format. I have my own team for the conversion. The website is for an electrician company called Brightwater electric. I have created a txt document with the project parameters and specifics. I have also uploaded their logo in all avaible formats. It's a zip file.

Number of Pages Required

1 page

```html
<!DOCTYPE html>
<html lang="en">
<head>
<meta charset="utf-8">
<title>Brightwater Electric</title>
<link href="https://fonts.googleapis.com/css2?family=Barlow+Condensed:wght@400;500;600;700&family=Poppins:wght@300;400;500;600;700;800&family=Roboto:wght@400;500;700&display=swap" rel="stylesheet">
<style>
:root{
  --red:#b51d24;
  --red-dark:#8f151b;
  --blue:#1565c0;
  --blue-dark:#0d4a93;
  --ink:#1c1c1e;
  --text:#444;
  --muted:#777;
  --white:#fff;
  --light:#f1f2f4;
}
*{margin:0;padding:0;box-sizing:border-box}
html,body{width:1200px;height:5000px;overflow:hidden;background:#fff}
body{font-family:"Roboto",sans-serif;color:var(--text)}
.page{position:relative;width:1200px;height:5000px;overflow:hidden}
.abs{position:absolute}
.cond{font-family:"Barlow Condensed",sans-serif}
.pop{font-family:"Poppins",sans-serif}

/* header */
.topbar{left:631px;top:0;width:569px;height:39px;display:flex}
.topbar .addr{background:var(--red);color:#fff;font-size:12px;white-space:nowrap;display:flex;align-items:center;gap:8px;padding:0 14px 0 26px;width:320px;clip-path:polygon(18px 0,100% 0,100% 100%,0 100%)}
.topbar .phone{background:var(--blue);color:#fff;font-size:18px;display:flex;align-items:center;gap:8px;padding:0 26px;flex:1;white-space:nowrap;font-family:"Barlow Condensed",sans-serif}
.brand{left:118px;top:6px;width:196px;height:140px;background:#fff;border-radius:0 0 98px 98px;display:flex;align-items:center;justify-content:center;gap:8px;z-index:3}
.brand .dot{width:16px;height:16px;border-radius:50%;background:var(--red)}
.brand span{font-family:"Barlow Condensed",sans-serif;font-weight:700;font-size:22px;color:var(--ink);text-transform:uppercase}
.nav{left:426px;top:66px;display:flex;gap:55px;font-family:"Barlow Condensed",sans-serif;font-size:16px;color:#333;letter-spacing:.5px}
.nav a{color:inherit;text-decoration:none}
.nav .on{color:var(--ink);font-weight:600;border-bottom:2px solid var(--red);padding-bottom:6px}

/* hero */
.hero{left:0;top:109px;width:1200px;height:633px;background:linear-gradient(90deg,#0d4a93 0%,#1565c0 40%,#5b87b8 65%,#c9ccd2 100%)}
.hero-kicker{left:122px;top:268px;color:#fff;font-family:"Poppins",sans-serif;font-size:17px;letter-spacing:3px}
.hero-title{left:122px;top:300px;border-left:3px solid #fff;padding-left:12px;color:#fff;font-family:"Barlow Condensed",sans-serif;font-weight:600;font-size:56px;line-height:50px;letter-spacing:1px}
.btn{display:inline-flex;align-items:center;justify-content:center;gap:8px;color:#fff;font-family:"Barlow Condensed",sans-serif;font-weight:600;font-size:18px;letter-spacing:.5px}
.hero-btn{left:122px;top:468px;width:170px;height:48px;background:var(--red)}

.fcard{color:#fff;text-align:center;display:flex;flex-direction:column;align-items:center;justify-content:center;padding:0 30px}
.fcard h3{font-family:"Barlow Condensed",sans-serif;font-weight:600;font-size:23px;letter-spacing:.5px;margin:6px 0 6px}
.fcard p{font-size:12px;line-height:17px;opacity:.85}
.fc1{left:132px;top:707px;width:309px;height:158px;background:var(--red)}
.fc2{left:441px;top:680px;width:322px;height:207px;background:var(--blue);box-shadow:0 10px 25px rgba(0,0,0,.25)}
.fc3{left:763px;top:707px;width:315px;height:158px;background:#2a2a2c}

/* about */
.about-frame{left:172px;top:1014px;width:416px;height:290px;border:2px solid var(--blue)}
.about-red{left:116px;top:1120px;width:245px;height:284px;background:var(--red)}
.about-img{left:134px;top:1029px;width:442px;height:362px;background:linear-gradient(135deg,#d9dadc,#a9abae 55%,#d4c54a)}
.kicker{font-family:"Poppins",sans-serif;font-size:14px;letter-spacing:2px;color:var(--blue)}
.h2{font-family:"Poppins",sans-serif;font-size:35px;color:var(--ink);font-weight:400}
.h2 b{color:var(--red);font-weight:800}
.about-text{left:642px;top:1077px;width:500px;font-size:17px;line-height:29.5px}
.divider{display:flex;align-items:center;gap:8px}
.divider i{display:block;width:48px;height:2px;background:currentColor}
.blue-btn{background:var(--blue);height:51px;width:180px}

/* services */
.svc-bg{left:0;top:1513px;width:1200px;height:672px;background:var(--ink)}
.svc-red{left:0;top:1513px;width:1200px;height:672px;background:linear-gradient(135deg,#c1161c,#8e1015);clip-path:polygon(885px 0,1200px 0,1200px 672px,440px 672px,440px 470px)}
.svc-head{left:0;top:1572px;width:1200px;text-align:center;color:#fff}
.scard{width:322px;height:350px}
.scard .ph{height:232px}
.scard .box{position:absolute;left:18px;right:18px;top:185px;height:165px;background:#fff;text-align:center;padding-top:22px}
.scard h4{font-family:"Roboto",sans-serif;font-weight:700;font-size:17px;color:var(--ink)}
.scard .ln{width:40px;height:2px;background:var(--blue);margin:8px auto 8px}
.scard p{font-size:16px;line-height:24px;color:#333}
.scard a{display:block;margin-top:10px;font-size:11px;font-weight:700;color:var(--red);text-decoration:underline}
.scard.act .box{background:var(--blue);top:185px;height:165px}
.scard.act h4,.scard.act p{color:#fff}
.scard.act .ln{background:#fff}
.scard.act a{color:#fff}

/* areas */
.area-frame{left:126px;top:2280px;width:172px;height:453px;border:3px solid var(--blue);border-right:none}
.area-list{left:173px;top:2498px;display:grid;grid-template-columns:185px 172px 150px;row-gap:28px;font-size:15px;color:var(--ink);font-weight:500}
.area-list div{display:flex;align-items:center;gap:8px}
.pin{width:24px;height:24px;border-radius:50%;background:var(--blue);display:inline-flex;align-items:center;justify-content:center}
.map{left:709px;top:2233px;width:437px;height:486px;background:linear-gradient(180deg,#f4f8fd,#e4edf8);border-radius:6px}

/* why */
.why-img{left:0;top:2845px;width:594px;height:567px;background:linear-gradient(160deg,#c7d2de,#3c5f9c 55%,#1f3d78)}
.why-bg{left:594px;top:2845px;width:606px;height:567px;background:linear-gradient(135deg,#0d55a8,#0a3e80)}
.why-item{display:flex;gap:18px;align-items:center;color:#fff}
.why-item .ic{width:58px;height:58px;border:2px solid rgba(255,255,255,.8);border-radius:50%;display:flex;align-items:center;justify-content:center;flex:none}
.why-item h5{font-size:17px;font-weight:700;color:#fff}
.why-item p{font-size:15px;color:rgba(255,255,255,.85);margin-top:3px}

/* gallery */
.gal{top:3591px;height:252px}

/* contact */
.contact-bg{left:0;top:4001px;width:1200px;height:586px;background:linear-gradient(90deg,#f4f4f5,#e9eaec)}
.form{left:550px;top:4094px;width:530px;height:386px;background:var(--red);border-radius:50px 0 50px 0}
.field{position:absolute;background:#fff;height:38px;font-size:12px;color:#555;padding:11px 14px}
.send{left:590px;top:4382px;width:170px;height:46px;border:1.5px solid #fff;color:#fff;font-size:13px;font-weight:600;display:flex;align-items:center;justify-content:center;letter-spacing:.5px}
.dots{background-image:radial-gradient(#555 1.3px,transparent 1.5px);background-size:12px 12px}
.ci{display:flex;align-items:center;gap:20px}
.ci .circ{width:44px;height:44px;border-radius:50%;background:var(--blue);display:flex;align-items:center;justify-content:center;flex:none}
.ci small{display:block;font-size:15px;color:var(--ink);margin-bottom:6px}
.ci b{font-size:16px;color:var(--ink);font-weight:500}

/* footer */
.footer{left:0;top:4587px;width:1200px;height:413px;background:#232325;color:#cfcfcf}
.fcol h6{font-family:"Barlow Condensed",sans-serif;font-size:20px;color:#fff;font-weight:500;letter-spacing:.5px;margin-bottom:14px}
.fcol li{list-style:none;font-size:12px;line-height:23px}
.vline{width:1px;background:#444}
.social{display:flex;gap:8px}
.social i{display:block;width:24px;height:24px;border-radius:50%;background:#fff}
</style>
</head>
<body>
<div class="page">

<!-- header -->
<div class="abs topbar">
  <div class="addr"><svg width="14" height="16" viewBox="0 0 14 16"><path d="M7 0a6 6 0 0 0-6 6c0 4.5 6 10 6 10s6-5.5 6-10a6 6 0 0 0-6-6z" fill="#fff"/><circle cx="7" cy="6" r="2.2" fill="#b51d24"/></svg>1420 Alder Ridge Rd Fairmont, MN 56031</div>
  <div class="phone"><svg width="18" height="18" viewBox="0 0 24 24"><circle cx="12" cy="12" r="12" fill="#fff"/><path d="M8 6l2 3-1.3 1.5a8 8 0 0 0 4.8 4.8L15 14l3 2-1 2.3C12 18 6 12 5.7 7z" fill="#1565c0"/></svg>555 014 2290</div>
</div>
<div class="abs brand"><i class="dot"></i><span>Brightwater</span></div>
<nav class="abs nav"><a class="on">COMPANY</a><a>SERVICE AREA</a><a>SERVICES</a><a>CONTACT</a><a>GALLERY</a><a>FAQS</a></nav>

<!-- hero -->
<div class="abs hero" role="img" aria-label="Electrician in a blue cap wiring a distribution panel"></div>
<div class="abs hero-kicker">BRIGHTWATER ELECTRIC</div>
<h1 class="abs hero-title">COMMERCIAL &amp;<br>RESIDENTIAL<br>ELECTRICAL SERVICE</h1>
<div class="abs btn hero-btn">CONTACT US <svg width="10" height="14" viewBox="0 0 10 14"><path d="M6 0L0 8h4l-1 6 7-8H6z" fill="#fff"/></svg></div>

<div class="abs fcard fc1">
  <svg width="36" height="36" viewBox="0 0 36 36" fill="none" stroke="#fff" stroke-width="1.5"><path d="M20 4L10 20h8l-3 12 12-17h-8z"/></svg>
  <h3>OUR COMPANY</h3><p>Lorem Ipsum is simply dummy text of the printing and typesetting industry.</p>
</div>
<div class="abs fcard fc2">
  <svg width="48" height="48" viewBox="0 0 48 48" fill="none" stroke="#fff" stroke-width="1.6"><circle cx="24" cy="24" r="20"/><path d="M26 12l-8 13h6l-2 11 9-14h-6z"/></svg>
  <h3>ELECTRICAL SERVICE</h3><p>Lorem Ipsum is simply dummy text of the printing and typesetting industry. Lorem I</p>
</div>
<div class="abs fcard fc3">
  <svg width="38" height="38" viewBox="0 0 24 24" fill="none" stroke="#fff" stroke-width="1.2"><path d="M6 3l3 4-2 2a11 11 0 0 0 8 8l2-2 4 3-2 3C10 21 3 14 3 5z"/></svg>
  <h3>CONTACT US</h3><p>1420 Alder Ridge Rd Fairmont, MN 56031<br><b>555 014 2290</b></p>
</div>

<!-- about -->
<div class="abs about-frame"></div>
<div class="abs about-red"></div>
<div class="abs about-img" role="img" aria-label="Worker in hard hat and safety vest installing ceiling wiring"></div>
<div class="abs kicker" style="left:643px;top:1026px">WHO WE ARE</div>
<h2 class="abs h2" style="left:640px;top:1042px">ABOUT <b>COMPANY</b></h2>
<div class="abs divider" style="left:643px;top:1088px;color:var(--blue)"><i style="width:30px"></i><svg width="10" height="14" viewBox="0 0 10 14"><path d="M6 0L0 8h4l-1 6 7-8H6z" fill="#1565c0"/></svg><i style="width:30px"></i></div>
<p class="abs about-text" style="top:1118px">Lorem ipsum dolor sit amet, consectetur adipiscing elit, sed do eiusmod tempor incididunt ut labore et dolore magna aliqua. Ut enim ad minim veniam, quis nostrud exercitation Allamco laboris nisi ut aliquip ex ea commodo consequat. Duis aute irure dolor in reprehenderit in voluptate velit esse Lorem ipsum dolor sit amet, consectetur.</p>
<div class="abs btn blue-btn" style="left:640px;top:1332px">LEARN MORE <svg width="10" height="14" viewBox="0 0 10 14"><path d="M6 0L0 8h4l-1 6 7-8H6z" fill="#fff"/></svg></div>
<div class="abs" style="left:812px;top:1332px;width:8px;height:51px;background:var(--red)"></div>

<!-- services -->
<div class="abs svc-bg"></div>
<div class="abs svc-red" role="img" aria-label="Red-toned photo of electrical wiring and tools"></div>
<div class="abs svc-head">
  <div class="pop" style="font-size:13px;font-weight:600;letter-spacing:2px">WHATWE DO</div>
  <div class="pop" style="font-size:34px;letter-spacing:1px;margin-top:2px">SERVICES <b style="font-weight:700">PROVIDE</b></div>
  <div class="divider" style="justify-content:center;margin-top:8px;color:#fff"><i></i><svg width="10" height="14" viewBox="0 0 10 14"><path d="M6 0L0 8h4l-1 6 7-8H6z" fill="#fff"/></svg><i></i></div>
</div>
<div class="abs scard" style="left:103px;top:1711px">
  <div class="ph" style="background:linear-gradient(135deg,#e9e9ea,#8a8f98)" role="img" aria-label="Electrician working on a residential wall outlet"></div>
  <div class="box"><h4>RESIDENTIAL ELECTRICAL</h4><div class="ln"></div><p>Lorem ipsum dolor sit amet,<br>consectetur adipiscing</p><a>LEARN MORE</a></div>
</div>
<div class="abs scard act" style="left:445px;top:1711px">
  <div class="ph" style="background:linear-gradient(135deg,#c77a3c,#d9b257 60%,#8a5a30)" role="img" aria-label="Electrician in yellow working at a building site"></div>
  <div class="box"><h4>COMMERCIAL ELECTRICAL</h4><div class="ln"></div><p>Lorem ipsum dolor sit amet,<br>consectetur adipiscing</p><a>LEARN MORE</a></div>
</div>
<div class="abs scard" style="left:788px;top:1711px">
  <div class="ph" style="background:linear-gradient(135deg,#c9c9c4,#7d8b5a 60%,#d6d1b0)" role="img" aria-label="Electrician in hard hat at an industrial panel"></div>
  <div class="box"><h4>INDUSTRIAL ELECTRICAL</h4><div class="ln"></div><p>Lorem ipsum dolor sit amet,<br>consectetur adipiscing</p><a>LEARN MORE</a></div>
</div>

<!-- service areas -->
<div class="abs area-frame"></div>
<div class="abs" style="left:296px;top:2283px;width:6px;height:70px;background:#fff"></div>
<div class="abs" style="left:296px;top:2610px;width:6px;height:120px;background:#fff"></div>
<div class="abs kicker" style="left:173px;top:2335px">OUR LOCATION</div>
<h2 class="abs h2" style="left:171px;top:2353px">SERVICE <b>AREAS</b></h2>
<div class="abs divider" style="left:173px;top:2402px;color:var(--blue)"><i style="width:60px"></i><svg width="10" height="14" viewBox="0 0 10 14"><path d="M6 0L0 8h4l-1 6 7-8H6z" fill="#1565c0"/></svg><i style="width:60px"></i></div>
<p class="abs" style="left:174px;top:2432px;width:490px;font-size:16px;line-height:26px;color:#444">Lorem ipsum dolor sit amet, consectetur adipiscing elit, sed do eiusmod tempor incididunt ut labore et dolore magn</p>
<div class="abs area-list">
  <div><span class="pin"><svg width="10" height="12" viewBox="0 0 14 16"><path d="M7 0a6 6 0 0 0-6 6c0 4.5 6 10 6 10s6-5.5 6-10a6 6 0 0 0-6-6z" fill="#fff"/></svg></span>Central Minnesota</div>
  <div><span class="pin"><svg width="10" height="12" viewBox="0 0 14 16"><path d="M7 0a6 6 0 0 0-6 6c0 4.5 6 10 6 10s6-5.5 6-10a6 6 0 0 0-6-6z" fill="#fff"/></svg></span>Sed ut perspiciat</div>
  <div><span class="pin"><svg width="10" height="12" viewBox="0 0 14 16"><path d="M7 0a6 6 0 0 0-6 6c0 4.5 6 10 6 10s6-5.5 6-10a6 6 0 0 0-6-6z" fill="#fff"/></svg></span>Location Area</div>
  <div><span class="pin"><svg width="10" height="12" viewBox="0 0 14 16"><path d="M7 0a6 6 0 0 0-6 6c0 4.5 6 10 6 10s6-5.5 6-10a6 6 0 0 0-6-6z" fill="#fff"/></svg></span>Lorem ipsum</div>
  <div><span class="pin"><svg width="10" height="12" viewBox="0 0 14 16"><path d="M7 0a6 6 0 0 0-6 6c0 4.5 6 10 6 10s6-5.5 6-10a6 6 0 0 0-6-6z" fill="#fff"/></svg></span>Quis autem</div>
  <div><span class="pin"><svg width="10" height="12" viewBox="0 0 14 16"><path d="M7 0a6 6 0 0 0-6 6c0 4.5 6 10 6 10s6-5.5 6-10a6 6 0 0 0-6-6z" fill="#fff"/></svg></span>Location Area</div>
</div>
<div class="abs btn blue-btn" style="left:177px;top:2626px;width:178px;height:50px">LEARN MORE <svg width="10" height="14" viewBox="0 0 10 14"><path d="M6 0L0 8h4l-1 6 7-8H6z" fill="#fff"/></svg></div>
<div class="abs map" role="img" aria-label="Outline map of Minnesota counties with service location pins"></div>

<!-- why choose -->
<div class="abs why-img" role="img" aria-label="Two electricians in blue workwear carrying cable and a toolbox"></div>
<div class="abs why-bg"></div>
<div class="abs kicker" style="left:669px;top:2930px;color:#fff;font-size:13px">WHY CHOOSE US</div>
<div class="abs pop" style="left:669px;top:2950px;color:#fff;font-size:29px;line-height:38px">WHY CHOOSE<br><b style="font-weight:700">BRIGHTWATER ELECTRIC</b></div>
<div class="abs divider" style="left:670px;top:3032px;color:#fff"><i style="width:54px"></i><svg width="10" height="14" viewBox="0 0 10 14"><path d="M6 0L0 8h4l-1 6 7-8H6z" fill="#fff"/></svg><i style="width:54px"></i></div>
<div class="abs why-item" style="left:666px;top:3076px"><div class="ic"><svg width="34" height="34" viewBox="0 0 34 34" fill="none" stroke="#fff" stroke-width="1.4"><circle cx="17" cy="17" r="13"/><text x="17" y="21" font-size="10" text-anchor="middle" fill="#fff" stroke="none" font-family="Roboto">24/7</text></svg></div><div><h5>24/7 Service</h5><p>Lorem ipsum dolor sit amet consect Lorem ipsum</p></div></div>
<div class="abs why-item" style="left:666px;top:3160px"><div class="ic"><svg width="30" height="30" viewBox="0 0 30 30" fill="none" stroke="#fff" stroke-width="1.4"><circle cx="15" cy="15" r="11"/><path d="M15 8v14M11 12h6a2 2 0 0 1 0 4h-4a2 2 0 0 0 0 4h6"/></svg></div><div><h5>Best Pricing</h5><p>Lorem ipsum dolor sit amet consect Lorem</p></div></div>
<div class="abs why-item" style="left:666px;top:3244px"><div class="ic"><svg width="30" height="30" viewBox="0 0 30 30" fill="none" stroke="#fff" stroke-width="1.4"><circle cx="15" cy="10" r="5"/><path d="M5 26c1-6 5-9 10-9s9 3 10 9"/></svg></div><div><h5>Experience Electrician</h5><p>Lorem ipsum dolor sit amet consect Lorem ipsum</p></div></div>

<!-- gallery -->
<div class="abs kicker" style="left:0;width:1200px;text-align:center;top:3474px;font-size:13px">OUR WORK</div>
<h2 class="abs h2" style="left:0;width:1200px;text-align:center;top:3490px;font-size:32px"><b>OUR</b> <span style="font-weight:700;color:var(--ink)">GALLERY</span></h2>
<div class="abs divider" style="left:0;width:1200px;justify-content:center;top:3540px;color:var(--blue)"><i style="width:58px"></i><svg width="10" height="14" viewBox="0 0 10 14"><path d="M6 0L0 8h4l-1 6 7-8H6z" fill="#1565c0"/></svg><i style="width:58px"></i></div>
<div class="abs gal" style="left:0;width:292px;background:linear-gradient(135deg,#e28a3a,#2d5d9b 60%,#1b3566)" role="img" aria-label="Electrician working on a large wiring cabinet"></div>
<div class="abs gal" style="left:301px;width:292px;background:linear-gradient(135deg,#8e979b,#d2d6c9 50%,#9bb54a)" role="img" aria-label="Electrician in hi-vis jacket inspecting a control panel"></div>
<div class="abs gal" style="left:606px;width:292px;background:linear-gradient(135deg,#eceef0,#b8bcc2 60%,#c5543a)" role="img" aria-label="Electrician on a ladder fitting a ceiling light"></div>
<div class="abs gal" style="left:910px;width:290px;background:linear-gradient(135deg,#c8cdd2,#e5e0d8 45%,#e07a2e 75%,#c9d447)" role="img" aria-label="Two engineers in hi-vis vests at an industrial site"></div>
<div class="abs btn blue-btn" style="left:501px;top:3888px;width:186px;height:52px">VIEW MORE <svg width="10" height="14" viewBox="0 0 10 14"><path d="M6 0L0 8h4l-1 6 7-8H6z" fill="#fff"/></svg></div>

<!-- contact -->
<div class="abs contact-bg" role="img" aria-label="Faded greyscale photo of an electrician at work"></div>
<div class="abs kicker" style="left:122px;top:4104px;color:var(--red);font-size:13px">GET IN TOUCH</div>
<h2 class="abs h2" style="left:121px;top:4119px;font-size:32px"><b>CONTACT</b> <span style="font-weight:700;color:var(--ink)">US</span></h2>
<div class="abs divider" style="left:122px;top:4164px;color:var(--blue)"><i style="width:64px"></i><svg width="10" height="14" viewBox="0 0 10 14"><path d="M6 0L0 8h4l-1 6 7-8H6z" fill="#1565c0"/></svg><i style="width:64px"></i></div>
<p class="abs" style="left:124px;top:4194px;width:350px;font-size:15px;line-height:22px;color:#444">Lorem ipsum dolor sit amet, consectetur adipiscing elit, sed do eiusmod tempor incididunt.</p>
<div class="abs ci" style="left:124px;top:4283px"><span class="circ"><svg width="16" height="20" viewBox="0 0 14 16"><path d="M7 0a6 6 0 0 0-6 6c0 4.5 6 10 6 10s6-5.5 6-10a6 6 0 0 0-6-6z" fill="#fff"/><circle cx="7" cy="6" r="2.2" fill="#1565c0"/></svg></span><div><small>ADDRESS:</small><b>1420 Alder Ridge Rd Fairmont, MN 56031</b></div></div>
<div class="abs ci" style="left:124px;top:4367px"><span class="circ"><svg width="20" height="20" viewBox="0 0 24 24"><path d="M6 3l3 4-2 2a11 11 0 0 0 8 8l2-2 4 3-2 3C10 21 3 14 3 5z" fill="#fff"/></svg></span><div><small>PHONE NUMBER</small><b style="font-size:18px">555 014 2290</b></div></div>
<div class="abs dots" style="left:812px;top:4310px;width:300px;height:190px;opacity:.55"></div>
<div class="abs form"></div>
<div class="field" style="left:592px;top:4148px;width:218px">First Name</div>
<div class="field" style="left:820px;top:4148px;width:218px">Last Name</div>
<div class="field" style="left:592px;top:4204px;width:218px">Email address</div>
<div class="field" style="left:820px;top:4204px;width:218px">Phone number</div>
<div class="field" style="left:592px;top:4260px;width:446px;height:110px">Message</div>
<div class="abs send">SEND MESSAGE</div>

<!-- footer -->
<div class="abs footer"></div>
<div class="abs" style="left:112px;top:4700px;display:flex;align-items:center;gap:8px"><i style="width:16px;height:16px;border-radius:50%;background:var(--red);display:block"></i><span class="cond" style="font-weight:700;font-size:24px;color:#fff">BRIGHTWATER</span></div>
<div class="abs social" style="left:166px;top:4814px"><i></i><i></i><i></i><i></i></div>
<div class="abs vline" style="left:428px;top:4640px;height:266px"></div>
<div class="abs vline" style="left:863px;top:4640px;height:266px"></div>
<div class="abs fcol" style="left:449px;top:4670px"><h6>NAVIGATION</h6><ul><li>Company</li><li>Service Area</li><li>Services</li><li>Contact</li><li>Gallery</li><li>FAQs</li></ul></div>
<div class="abs fcol" style="left:632px;top:4670px"><h6>SERVICES</h6><ul><li>Commerical Electrical Services</li><li>Residential Electrical Services</li><li>Industrial Electrical Services</li></ul></div>
<div class="abs fcol" style="left:884px;top:4670px"><h6>CONTACT US</h6>
  <div style="display:flex;gap:10px;font-size:12px;line-height:17px"><span class="pin" style="background:#fff;flex:none"><svg width="10" height="12" viewBox="0 0 14 16"><path d="M7 0a6 6 0 0 0-6 6c0 4.5 6 10 6 10s6-5.5 6-10a6 6 0 0 0-6-6z" fill="#232325"/></svg></span><div>Address<br>1420 Alder Ridge Rd<br>Fairmont, MN 56031</div></div>
  <div style="display:flex;gap:10px;font-size:12px;align-items:center;margin-top:12px"><span class="pin" style="background:#fff"><svg width="12" height="12" viewBox="0 0 24 24"><path d="M6 3l3 4-2 2a11 11 0 0 0 8 8l2-2 4 3-2 3C10 21 3 14 3 5z" fill="#232325"/></svg></span><div>Phone: <b style="color:#fff">555 014 2290</b></div></div>
</div>
<div class="abs" style="left:0;top:4960px;width:1200px;height:1px;background:#3a3a3c"></div>
<div class="abs" style="left:0;top:4973px;width:1200px;text-align:center;font-size:11px;color:#999">© 2022 Brightwater Electric . All Rights Reserved</div>

</div>
</body>
</html>
```